Webpage layout and company logo combination

We are trying to renovate an existing site to make it sharper and sophisticated in appearance. This is the existing site: http://www.kestrelhomesnj.com/agents.html . The new presentation should be bright, sharp, sophisticated and should incorporate two additional menu tabs. The menu tabs will be revised as follows: Property Listings, Property Management, Advisory & Consulting, Local Info, R/E Tools, Our Team (please disregard Korean language characters, which will be installed after English version is completed, separately).

It Company

```html
<!DOCTYPE html>
<html lang="en">
<head>
<meta charset="utf-8">
<title>Kestrel Homes</title>
<link href="https://fonts.googleapis.com/css2?family=Roboto:wght@400;500;700&display=swap" rel="stylesheet">
<style>
:root{
  --bg:#ececec;
  --paper:#ffffff;
  --rose:#a84f70;
  --rose-light:#c8809a;
  --rose-dark:#7a2c4a;
  --ink:#444444;
  --rule:#dddddd;
  --dark:#333333;
  --darker:#2a2a2a;
  --line-dark:#555555;
}
*{box-sizing:border-box;margin:0;padding:0}
html,body{width:809px;height:1200px;overflow:hidden}
body{background:var(--bg);font-family:"Roboto",Arial,sans-serif;color:var(--ink);position:relative}
.abs{position:absolute}
.brand{left:118px;top:33px;display:flex;align-items:center;gap:8px}
.brand-mark{width:26px;height:26px;border-radius:50%;background:var(--rose)}
.brand-name{font-size:21px;font-weight:500;color:var(--rose);letter-spacing:.3px}
.phone{right:234px;top:28px;display:flex;align-items:center;gap:7px;font-size:13px;line-height:16px;color:var(--rose-dark);white-space:nowrap}
.btn-consult{left:588px;top:26px;width:105px;height:20px;border-radius:4px;background:linear-gradient(#c67b97,#a04868);color:#fff;font-size:9.5px;font-weight:500;text-align:center;line-height:20px;white-space:nowrap}
.page{left:116px;top:70px;width:577px;height:1130px;background:var(--paper);box-shadow:0 0 6px rgba(0,0,0,.12)}
.nav{left:130px;top:90px;width:549px;height:24px;border-radius:3px;background:linear-gradient(#c8809a,#a04868);display:flex;align-items:center;justify-content:space-between;padding:0 7px;list-style:none}
.nav li{color:#fff;font-size:8.5px;font-weight:500;white-space:nowrap;padding-right:8px;border-right:1px solid rgba(255,255,255,.35)}
.nav li:last-child{border:0;padding-right:0}
.hero{left:130px;top:121px;width:549px;height:243px;background:linear-gradient(180deg,#c79a3c 0%,#e3b24a 28%,#6b6a5a 55%,#3f4a32 78%,#8a8a82 100%)}
.arrow{top:232px;width:35px;height:24px;background:rgba(20,20,20,.75);display:flex;align-items:center;justify-content:center}
.search{left:424px;top:149px;width:223px;height:192px;background:rgba(255,255,255,.78);border-radius:2px}
.search h2{position:absolute;left:0;top:10px;width:100%;text-align:center;font-size:17px;font-weight:700;color:var(--rose-dark)}
.orn-rule{position:absolute;left:60px;top:40px;width:103px;height:1px;background:var(--rose-dark)}
.field{position:absolute;height:20px;background:#fff;border:1px solid #ddd;border-radius:2px;font-size:8.5px;color:#aaa;padding-left:9px;line-height:18px}
.field i{position:absolute;right:5px;top:5px;width:9px;height:8px;background:#eee;border:1px solid #888}
.search-btn{position:absolute;left:20px;top:149px;width:186px;height:23px;border-radius:2px;background:linear-gradient(#c67b97,#9a4464);color:#fff;font-size:11px;font-weight:700;letter-spacing:1px;text-align:center;line-height:23px}
.steps{left:130px;top:370px;width:549px;height:32px;background:linear-gradient(#3a3a3a,#151515);border-radius:2px}
.step{position:absolute;top:0;height:32px;line-height:32px;color:#fff;font-size:7.5px;font-weight:700;text-transform:uppercase;white-space:nowrap}
.step b{position:absolute;top:-3px;width:14px;height:14px;border-radius:50%;background:var(--rose);font-size:7px;line-height:14px;text-align:center}
.h-section{font-size:17px;font-weight:700;color:var(--rose);white-space:nowrap}
.rule{height:1px;background:var(--rule)}
.copy{font-size:8px;line-height:12.2px;color:var(--ink)}
.ticks{list-style:none;left:372px;top:469px}
.ticks li{font-size:8px;height:13.4px;display:flex;align-items:center;gap:9px;white-space:nowrap}
.photo{position:absolute}
.overlay{background:rgba(168,79,112,.82);display:flex;flex-direction:column;align-items:center;justify-content:center;gap:8px;color:#fff;font-size:7.5px}
.ov-icons{display:flex;gap:5px}
.ov-icons span{width:15px;height:15px;border:1px solid #fff;border-radius:50%}
.footer{left:130px;top:978px;width:549px;height:172px;background:var(--dark)}
.fcol{position:absolute;top:0;height:172px}
.fh{position:absolute;top:17px;display:flex;align-items:center;gap:8px;color:#fff;font-size:12px;font-weight:500;white-space:nowrap}
.news-date{color:var(--rose-light);font-size:8px}
.news-text{color:#fff;font-size:8px;line-height:10px}
.contact-list{position:absolute;left:16px;top:48px;width:150px;height:110px}
.contact-row{position:absolute;left:0;width:150px;display:flex;align-items:flex-start;gap:8px;color:#fff;font-size:8px;line-height:9.5px}
.contact-row svg{flex:none;margin-top:1px}
.social{position:absolute;left:0;top:75px;display:flex;gap:7px}
.social span{width:14px;height:14px;background:#fff;border-radius:2px}
.email{position:absolute;top:75px;width:140px;height:20px;background:#fff;border:1px solid #bbb;font-size:8px;color:#aaa;padding-left:10px;line-height:18px}
.submit{position:absolute;top:108px;width:46px;height:22px;border-radius:3px;background:linear-gradient(#c67b97,#9a4464);color:#fff;font-size:9px;text-align:center;line-height:22px}
.copyright{left:130px;top:1150px;width:549px;height:22px;background:var(--rose);color:#fff;font-size:8px;text-align:center;line-height:22px}
.skyline{left:116px;top:1125px;width:577px;height:75px;background:linear-gradient(rgba(200,200,200,0),rgba(200,200,200,.55))}
</style>
</head>
<body>

<div class="abs brand"><span class="brand-mark"></span><span class="brand-name">Kestrel Homes</span></div>
<div class="abs phone">
  <svg width="13" height="13" viewBox="0 0 14 14"><circle cx="7" cy="7" r="6" fill="none" stroke="#7a2c4a" stroke-width="1.4"/><path d="M5 4.2l1 .9-.6 1c.4.8 1 1.4 1.8 1.8l1-.6.9 1-.8.9C6.5 9 5 7.5 4.2 5.3z" fill="#7a2c4a"/></svg>
  (866)555-0142
</div>
<div class="abs btn-consult">Book a Consultation</div>

<div class="abs page"></div>

<ul class="abs nav">
  <li>About Us</li><li>Property Listings</li><li>Property Management</li><li>Advisory &amp; Consulting</li><li>Local Info</li><li>R/E Tools</li><li>Our Team</li><li>Contact Us</li>
</ul>

<div class="abs hero" role="img" aria-label="Modern house with a curved driveway at sunset"></div>
<div class="abs arrow" style="left:130px"><svg width="10" height="14"><path d="M8 1L2 7l6 6" stroke="#fff" stroke-width="2" fill="none"/></svg></div>
<div class="abs arrow" style="left:644px"><svg width="10" height="14"><path d="M2 1l6 6-6 6" stroke="#fff" stroke-width="2" fill="none"/></svg></div>

<form class="abs search">
  <h2>Find Your Dream Home</h2>
  <span class="orn-rule"></span>
  <div class="field" style="left:20px;top:64px;width:186px">City<i></i></div>
  <div class="field" style="left:20px;top:91px;width:186px">Property Type<i></i></div>
  <div class="field" style="left:20px;top:119px;width:86px">Price Min<i></i></div>
  <div class="field" style="left:119px;top:119px;width:87px">Price Max<i></i></div>
  <div class="search-btn">SEARCH HOME</div>
</form>

<div class="abs steps">
  <svg class="abs" style="left:0;top:0" width="549" height="32"><g stroke="#fff" stroke-width="1.2" fill="none"><path d="M130 0l12 16-12 16"/><path d="M270 0l12 16-12 16"/><path d="M409 0l12 16-12 16"/></g></svg>
  <div class="step" style="left:18px">Book a Consultation<b style="left:-15px">1</b></div>
  <div class="step" style="left:169px">Choose a Design<b style="left:-23px">2</b></div>
  <div class="step" style="left:293px">Create your New Home<b style="left:-8px">3</b></div>
  <div class="step" style="left:434px">Handing over the Keys<b style="left:-12px">4</b></div>
</div>

<h2 class="abs h-section" style="left:132px;top:424px">Welcome to Kestrel Homes</h2>
<div class="abs rule" style="left:130px;top:450px;width:215px"></div>
<h2 class="abs h-section" style="left:369px;top:424px">Why Us?</h2>
<div class="abs rule" style="left:369px;top:450px;width:310px"></div>

<div class="abs copy" style="left:132px;top:467px;width:212px">
  <p>Quisque eu erat urna. In hac habitasse platea dictumst. Ut et lorem at elit congue facilisis. Aliquam malesuada quis dolor sed euismod. Proin sit amet mauris quis magna volutpat semper id vitae augue. Cras consectetur, neque rhoncus cursus commodo, eros sem facilisis orci, vitae cursus eros tellus quis eros.</p>
  <p style="margin-top:12px">Suspendisse potenti. Nam ante justo, volutpat quis sodales a, tincidunt sed erat. Vivamus fermentum ante nunc, id accumsan libero bibendum a. Duis venenatis nibh ac convallis laoreet. In dignissim imperdiet feugiat. Integer blandit tortor tellus, sed sodales ligula tristique et. Integer mattis consequat sem ac vestibulum. Maecenas ut ante euismod, suscipit risus sit amet, consectetur felis.</p>
</div>

<ul class="abs ticks">
  <li><svg width="9" height="9"><circle cx="4.5" cy="4.5" r="4.5" fill="#444"/><path d="M2.3 4.6l1.6 1.5 2.9-3" stroke="#fff" stroke-width="1.2" fill="none"/></svg>Nulla congue suscipit semper</li>
  <li><svg width="9" height="9"><circle cx="4.5" cy="4.5" r="4.5" fill="#444"/><path d="M2.3 4.6l1.6 1.5 2.9-3" stroke="#fff" stroke-width="1.2" fill="none"/></svg>Quisque a dictum diam</li>
  <li><svg width="9" height="9"><circle cx="4.5" cy="4.5" r="4.5" fill="#444"/><path d="M2.3 4.6l1.6 1.5 2.9-3" stroke="#fff" stroke-width="1.2" fill="none"/></svg>Nulla tristique turpis pretium Luctus</li>
  <li><svg width="9" height="9"><circle cx="4.5" cy="4.5" r="4.5" fill="#444"/><path d="M2.3 4.6l1.6 1.5 2.9-3" stroke="#fff" stroke-width="1.2" fill="none"/></svg>Praesent malesuada, magna</li>
  <li><svg width="9" height="9"><circle cx="4.5" cy="4.5" r="4.5" fill="#444"/><path d="M2.3 4.6l1.6 1.5 2.9-3" stroke="#fff" stroke-width="1.2" fill="none"/></svg>Ut et lorem at elit congue facilisis</li>
  <li><svg width="9" height="9"><circle cx="4.5" cy="4.5" r="4.5" fill="#444"/><path d="M2.3 4.6l1.6 1.5 2.9-3" stroke="#fff" stroke-width="1.2" fill="none"/></svg>Aliquam malesuada quis dolor sed</li>
</ul>
<div class="photo" role="img" aria-label="White modern villa terrace overlooking a green lawn" style="left:543px;top:469px;width:136px;height:77px;background:linear-gradient(180deg,#7fb0d8 0%,#b9d3e6 45%,#7a9a50 75%,#5a7a3a 100%)"></div>
<p class="abs copy" style="left:373px;top:553px;width:300px">quis magna volutpat semper id vitae augue. Cras consectetur, neque rhoncus cursus commodo, eros sem facilisis orci, vitae cursus eros tellus quis eros. Etiam non accumsan dolor. Pellentesque condimentum sollicitudin augue, in malesuada nulla facilisis eu. Sed elementum commodo urna quis varius. Integer pulvinar sagittis est, eget convallis nunc viverra et. Cras sit amet dignissim magna, id volutpat erat.</p>

<h2 class="abs h-section" style="left:132px;top:660px">Featured Holiday Accomodation</h2>
<div class="abs rule" style="left:130px;top:686px;width:549px"></div>

<div class="photo" role="img" aria-label="Holiday villa with swimming pool and loungers" style="left:130px;top:709px;width:273px;height:120px;background:linear-gradient(180deg,#8aa8c8 0%,#d8d4cc 45%,#c8c4bc 70%,#3a8ac0 100%)"></div>
<div class="photo" role="img" aria-label="Bedroom with a blue bedspread and brass bed frame" style="left:405px;top:709px;width:274px;height:120px;background:linear-gradient(135deg,#c89a5a 0%,#e8e0d0 40%,#3a3a80 75%,#2a2a60 100%)"></div>
<div class="photo" role="img" aria-label="Stone cottage with pink flowers in front" style="left:130px;top:831px;width:181px;height:118px;background:linear-gradient(180deg,#8aa0b8 0%,#6a6a6a 30%,#c8a0a0 60%,#4a8a3a 100%)"></div>
<div class="photo" role="img" aria-label="Cosy living room with fireplace and armchairs" style="left:313px;top:831px;width:182px;height:118px;background:linear-gradient(135deg,#7a5a3a 0%,#c8a880 45%,#a8987a 70%,#6a7888 100%)"></div>
<div class="photo" role="img" aria-label="Bright guest bedroom" style="left:497px;top:831px;width:182px;height:118px;background:linear-gradient(135deg,#d8c8b8,#b8a090)"></div>
<div class="photo overlay" style="left:497px;top:831px;width:182px;height:118px">
  <div class="ov-icons"><span></span><span></span></div>
  <div>Price from $220 p/n*</div>
</div>

<div class="abs skyline" role="img" aria-label="Faint city skyline silhouette"></div>

<footer class="abs footer">
  <div class="fcol" style="left:0;width:196px">
    <div class="fh" style="left:12px"><svg width="18" height="15"><rect x="1" y="1" width="16" height="13" fill="none" stroke="#fff" stroke-width="1.5"/><path d="M4 5h10M4 8h10M4 11h6" stroke="#fff"/></svg>Latest News</div>
    <div style="position:absolute;left:10px;top:46px;width:170px">
      <div class="news-date">6th March, 2014</div>
      <div class="news-text">Nulla congue suscipit semper. Quisque a dictum diam. Nulla tristique turpis</div>
    </div>
    <div class="rule" style="position:absolute;left:10px;top:86px;width:168px;background:var(--line-dark)"></div>
    <div style="position:absolute;left:10px;top:98px;width:170px">
      <div class="news-date">6th March, 2014</div>
      <div class="news-text">Nulla congue suscipit semper. Quisque a dictum diam. Nulla tristique turpis</div>
    </div>
    <div class="rule" style="position:absolute;left:10px;top:137px;width:168px;background:var(--line-dark)"></div>
    <div style="position:absolute;left:154px;top:146px;color:#fff;font-size:7.5px;text-decoration:underline;white-space:nowrap">View all »</div>
  </div>
  <div class="fcol" style="left:196px;width:174px;background:var(--darker)">
    <div class="fh" style="left:20px"><svg width="16" height="15"><rect x="1" y="2" width="12" height="12" fill="none" stroke="#fff" stroke-width="1.5"/><path d="M6 9l9-8M10 1h5v5" stroke="#fff" stroke-width="1.6" fill="none"/></svg>Contact Us</div>
    <div class="contact-list">
      <div class="contact-row" style="top:0"><svg width="9" height="9"><path d="M4.5 0L9 4H7.5v5h-6V4H0z" fill="#fff"/></svg><span>418 Linden Crest Road Oakvale,<br>NJ 07990</span></div>
      <div class="contact-row" style="top:29px"><svg width="9" height="9"><path d="M1.5 0l2 2-1 1.5c.7 1.4 1.6 2.3 3 3L7 5.5l2 2L7.5 9C3.5 8.5.5 5.5 0 1.5z" fill="#fff"/></svg><span>(866)555-0142</span></div>
      <div class="contact-row" style="top:51px"><svg width="9" height="9"><rect y="1.5" width="9" height="6" fill="#fff"/><path d="M0 1.5l4.5 3.5L9 1.5" stroke="#333" fill="none"/></svg><span>info@kestrelhomesnj.com</span></div>
      <div class="social"><span></span><span></span><span></span><span></span></div>
    </div>
  </div>
  <div class="fcol" style="left:380px;width:169px">
    <div class="fh" style="left:10px"><svg width="18" height="14"><rect x="1" y="1" width="16" height="12" fill="none" stroke="#fff" stroke-width="1.5"/><path d="M4 4h3M9 4h5M4 7h3M9 7h5M4 10h10" stroke="#fff"/></svg>Subscribe Newsletter</div>
    <p style="position:absolute;left:15px;top:45px;width:145px;color:#fff;font-size:8px;line-height:10px">Enter your email address to reiceive all news from our awesome website</p>
    <div class="email" style="left:18px">enter email address</div>
    <div class="submit" style="left:112px">Submit</div>
  </div>
</footer>
<div class="abs copyright">Copyright © 2014, All rights reserved.</div>

</body>
</html>
```